Bright Harbor Charity - helping the disadvantaged

I would like a new web site design for my charity BRIGHT HARBOR. The charity provides help for the disadvantaged. See current site
brightharbor.org.au for details. Please refer to the current site for information on the charity. The objectives of the charity are in the "about us" tab. You will also notice on the site that we provide information about events that we sponsor an area for this should be provided on the site.

Target Market(s)

We have two targets:
1. Individuals and Businesses that will donate money to the charity.
2. Individuals that are in need of support from the charity.

Industry/Entity Type

Charity

Requirements
Must have
• Ability for individuals to be able to understand the type of support we can provide.
Nice to have
• Our logo should be prominate on each pages
Should not have
• Should be use modern fonts

```html
<!DOCTYPE html>
<html lang="en">
<head>
<meta charset="utf-8">
<title>Bright Harbor – Helping the Disadvantaged</title>
<link rel="stylesheet" href="https://fonts.googleapis.com/css2?family=Play:wght@400;700&family=Open+Sans:wght@400;600;700&family=Arimo:wght@400;700&display=swap">
<style>
:root{
  --green:#55c91b;
  --green-dark:#3f9e12;
  --orange:#f2923b;
  --orange-dark:#cf6a1a;
  --text:#555;
  --text-dark:#333;
  --page:#f1f1ef;
  --panel:#f7f7f6;
  --line:#dcdcdc;
}
*{box-sizing:border-box;margin:0;padding:0}
html,body{width:1158px;height:1200px;overflow:hidden}
body{position:relative;background:var(--page);font-family:"Open Sans",sans-serif;color:var(--text)}
.abs{position:absolute}

/* nav */
.main-nav{left:0;top:0;width:1158px;height:35px;background:linear-gradient(#62d424,#4dbe16);border-bottom:3px solid var(--orange)}
.main-nav a{position:absolute;top:10px;transform:translateX(-50%);color:#fff;font:400 13px "Open Sans",sans-serif;text-decoration:none;white-space:nowrap}
.nav-active{left:111px;top:0;width:63px;height:41px;background:linear-gradient(#f6a457,#e27c24);border-radius:0 0 4px 4px;box-shadow:0 2px 2px rgba(0,0,0,.2)}

/* header */
.btn-email{left:777px;top:50px;width:115px;height:33px;border:2px dotted #e4524a;background:#fff;color:#e0323a;font:600 14px "Play",sans-serif;display:flex;align-items:center;justify-content:center}
.btn-sponsor{left:908px;top:50px;width:143px;height:33px;background:linear-gradient(#f39a4a,#e07a26);border:2px dotted #fff;outline:1px solid #e07a26;color:#fff;font:600 14px "Play",sans-serif;display:flex;align-items:center;justify-content:center}
.brand{left:123px;top:80px;display:flex;align-items:center;gap:10px}
.brand-mark{width:20px;height:20px;border-radius:50%;background:var(--orange)}
.brand-name{font:400 38px "Play",sans-serif;color:var(--green);letter-spacing:1px}
.tagline{right:113px;top:132px;font:400 19px "Open Sans",sans-serif;color:#555}
.tagline strong{color:var(--green);font-weight:700;font-size:23px}

/* slider */
.slider{left:107px;top:176px;width:945px;height:346px;background:linear-gradient(#f7a85c,#d8782a);border-radius:10px 10px 0 0}
.slider-inner{left:14px;top:13px;width:920px;height:321px;background:#fff}
.slider-photo{left:5px;top:5px;width:909px;height:311px;background:linear-gradient(90deg,#d9a979,#efd7b6 45%,#e6b27e 75%,#d29d6f)}
.slider-arrow{width:44px;height:44px;border-radius:50%;background:#fff;border:3px solid #888;display:flex;align-items:center;justify-content:center;top:149px}

/* announcements */
.announce{left:146px;top:569px;width:598px;height:381px;background:var(--panel)}
.section-title{font:700 21px "Play",sans-serif;color:#555;letter-spacing:.5px}
.section-title em{font-style:normal;color:var(--green)}
.post-title{left:28px;top:78px;font:700 22px "Play",sans-serif;color:#555}
.byline{left:32px;top:113px;font:400 11px "Arimo",sans-serif;color:#888}
.byline b{color:#333}
.post-photo{left:28px;top:148px;width:160px;height:150px;border:3px solid #fff;box-shadow:0 1px 3px rgba(0,0,0,.3);background:linear-gradient(160deg,#3c8a2a,#6fb04a 60%,#2f6f24)}
.post-body{left:208px;top:150px;width:345px;font:400 11.5px/21px "Open Sans",sans-serif;color:#555;text-align:justify}
.post-body b{color:#333}
.more{left:204px;top:299px;font:600 12px "Arimo",sans-serif;color:#333}
.rule{height:0;border-top:1px dotted #ccc}
.filed{left:32px;top:350px;font:400 11px "Arimo",sans-serif;color:#888;display:flex;align-items:center;gap:6px}
.filed b{color:#333}

.date-badge{left:98px;top:642px;width:49px;height:56px;background:#2e2e2e;color:#fff;text-align:center}
.date-badge .day{font:400 26px/30px "Play",sans-serif;margin-top:5px}
.date-badge .mon{font:400 11px "Arimo",sans-serif;color:#ccc}
.count{left:98px;width:49px;height:20px;color:#fff;font:700 11px "Arimo",sans-serif;display:flex;align-items:center;gap:10px;padding-left:8px}

.pager{left:239px;top:978px;display:flex;gap:4px}
.pager span{height:20px;min-width:20px;padding:0 5px;border:1px solid #999;background:#fff;font:400 10.5px/18px "Arimo",sans-serif;color:#333;text-align:center}
.pager .info{color:#777;margin-right:2px}
.pager .current{background:var(--orange);color:#fff;border-color:var(--orange-dark)}

/* sidebar */
.pay-banner{left:780px;top:544px;width:266px;height:37px}
.involved{left:780px;top:606px;width:254px;height:195px;border:3px dotted var(--orange);outline:1px solid var(--orange);background:#fff;overflow:hidden}
.involved-item{position:absolute;left:72px;font:400 13px/15px "Open Sans",sans-serif;color:#333;letter-spacing:.3px;width:150px}
.item-icon{position:absolute;left:20px}
.ribbon{right:-52px;top:20px;width:180px;height:38px;background:var(--orange);color:#fff;font:700 11px/14px "Arimo",sans-serif;text-align:center;padding-top:5px;transform:rotate(45deg)}
.test-text{left:787px;top:881px;width:240px;font:400 11px/19.3px "Open Sans",sans-serif;color:#666;text-align:justify}
.quote-mark{font:700 40px/40px "Play",sans-serif;color:#aaa}

/* footer */
.footer{left:0;top:1083px;width:1158px;height:117px;border-top:4px solid var(--green);background:linear-gradient(#f59b48,#c56c22)}
.footer-links{top:37px;width:100%;text-align:center;font:400 12.5px "Arimo",sans-serif;color:#fff}
.footer-links span{margin:0 6px}
.copyright{top:67px;width:100%;text-align:center;font:400 12.5px "Arimo",sans-serif;color:#fff}
</style>
</head>
<body>

<nav class="main-nav abs">
  <div class="nav-active abs"></div>
  <a style="left:142px">Home</a>
  <a style="left:245px">About Us</a>
  <a style="left:355px">Donate</a>
  <a style="left:455px">Apply</a>
  <a style="left:560px">Pledge</a>
  <a style="left:671px">Nominate</a>
  <a style="left:787px">Events</a>
  <a style="left:896px">Contact Us</a>
  <a style="left:1017px">Directors</a>
</nav>

<div class="btn-email abs">EMAIL SIGN-UP</div>
<div class="btn-sponsor abs">SPONSOR/DONATE</div>

<div class="brand abs">
  <div class="brand-mark"></div>
  <div class="brand-name">BRIGHT HARBOR</div>
</div>
<div class="tagline abs">Emergency Services provided assistance for <strong>25,000</strong> people last year</div>

<section class="slider abs">
  <div class="slider-inner abs">
    <div class="slider-photo abs" role="img" aria-label="Photo of six smiling children lying side by side with chins in their hands"></div>
  </div>
  <div class="slider-arrow abs" style="left:24px">
    <svg width="16" height="22" viewBox="0 0 16 22"><path d="M12 2 3 11l9 9" fill="none" stroke="#666" stroke-width="4"/></svg>
  </div>
  <div class="slider-arrow abs" style="left:874px">
    <svg width="16" height="22" viewBox="0 0 16 22"><path d="M4 2l9 9-9 9" fill="none" stroke="#666" stroke-width="4"/></svg>
  </div>
</section>

<section class="announce abs">
  <svg class="abs" style="left:10px;top:12px" width="42" height="36" viewBox="0 0 42 36">
    <path d="M4 13h8l20-10v30L12 23H4z" fill="#e8e8e8" stroke="#999" stroke-width="1.5"/>
    <path d="M26 6v24" stroke="var(--orange)" stroke-width="6"/>
    <path d="M9 23l3 11h5l-2-11" fill="#bbb"/>
  </svg>
  <h2 class="section-title abs" style="left:57px;top:17px"><em>ANNOUN</em>CEMENTS</h2>
  <div class="rule abs" style="left:28px;top:53px;width:540px"></div>
  <h3 class="post-title abs">Harmony Day Information Sheet &amp; Booking Form</h3>
  <div class="byline abs">Written by <b>Daniel Whitcombe</b></div>
  <div class="post-photo abs" role="img" aria-label="Photo of two young boys blowing bubbles on a lawn"></div>
  <p class="post-body abs"><b>Lorem Ipsum is simply dummy text of the printing and typesetting industry. Lorem</b> Ipsum has been the industry's standard dummy text ever since the 1500s, when an unknown printer took a galley of type and scrambled it to make a type specimen book. It has survived not only five centuries, to make a type specimen book. It has survived not only five centuries,</p>
  <div class="more abs">(more...) &nbsp;
    <svg width="16" height="9" viewBox="0 0 16 9"><path d="M0 0l5 4.5L0 9zM5.5 0l5 4.5-5 4.5zM11 0l5 4.5-5 4.5z" fill="#333"/></svg>
  </div>
  <div class="rule abs" style="left:28px;top:333px;width:535px"></div>
  <div class="filed abs">
    <svg width="13" height="14" viewBox="0 0 13 14"><path d="M1 1h8l3 3v9H1z" fill="#fff" stroke="#444"/></svg>
    <span><b>Filed under:</b> Featured Today, Uncategorized</span>
  </div>
</section>

<div class="date-badge abs"><div class="day">09</div><div class="mon">SEP</div></div>
<div class="count abs" style="top:705px;background:var(--green)">
  <svg width="12" height="11" viewBox="0 0 12 11"><path d="M6 1C3 1 1 2.7 1 4.8c0 1.2.7 2.2 1.8 2.9L2.3 10l2.6-1.5c.4.1.7.1 1.1.1 3 0 5-1.7 5-3.8S9 1 6 1z" fill="#fff"/></svg>0</div>
<div class="count abs" style="top:731px;background:#8a8a8a">
  <svg width="12" height="12" viewBox="0 0 12 12"><path d="M3 4a4 4 0 1 1 0 4" fill="none" stroke="#fff" stroke-width="2"/><path d="M1 1v4h4z" fill="#fff"/></svg>0</div>

<div class="pager abs">
  <span class="info">Page 1 of 11</span>
  <span class="current">1</span><span>2</span><span>3</span><span>4</span><span>5</span><span>»</span><span>10</span><span>...</span><span>Last »</span>
</div>

<aside>
  <svg class="pay-banner abs" viewBox="0 0 266 37">
    <path d="M0 0h250l16 18.5L250 37H0z" fill="var(--green)"/>
    <path d="M3 3h245l13 15.5L248 34H3z" fill="none" stroke="#fff" stroke-width="1" stroke-dasharray="2 2"/>
    <text x="13" y="24" font-family="Arimo, sans-serif" font-weight="700" font-size="13.5" fill="#fff">PAY IN FUNDRAISING MONEY NOW</text>
  </svg>

  <div class="involved abs">
    <div class="ribbon abs">GET<br>INVOLVED</div>
    <svg class="item-icon" style="top:14px" width="28" height="26" viewBox="0 0 28 26"><circle cx="14" cy="13" r="11" fill="#fff" stroke="var(--orange)" stroke-width="2"/><text x="14" y="17" text-anchor="middle" font-size="11" font-weight="700" fill="var(--orange)" font-family="Arimo,sans-serif">£</text></svg>
    <div class="involved-item" style="top:20px">Donate now</div>
    <svg class="item-icon" style="top:46px" width="28" height="34" viewBox="0 0 28 34"><path d="M9 2h10l-3 7c7 3 10 10 8 17-1 5-19 5-20 0-2-7 1-14 8-17z" fill="#fff" stroke="var(--orange)" stroke-width="2"/><text x="14" y="27" text-anchor="middle" font-size="10" font-weight="700" fill="var(--orange)" font-family="Arimo,sans-serif">£</text></svg>
    <div class="involved-item" style="top:50px">Pay in fundraising money</div>
    <svg class="item-icon" style="top:89px" width="28" height="34" viewBox="0 0 28 34"><path d="M9 2h10l-3 7c7 3 10 10 8 17-1 5-19 5-20 0-2-7 1-14 8-17z" fill="#fff" stroke="var(--orange)" stroke-width="2"/><text x="14" y="27" text-anchor="middle" font-size="10" font-weight="700" fill="var(--orange)" font-family="Arimo,sans-serif">£</text></svg>
    <div class="involved-item" style="top:93px">Pay in schools &amp; early years cash</div>
    <svg class="item-icon" style="top:142px;left:16px" width="34" height="20" viewBox="0 0 34 20"><rect x="8" y="3" width="24" height="15" fill="#fff" stroke="var(--orange)" stroke-width="1.5"/><path d="M8 3l12 9 12-9" fill="none" stroke="var(--orange)" stroke-width="1.5"/><path d="M0 7h5M1 11h4M0 15h5" stroke="var(--orange)"/></svg>
    <div class="involved-item" style="top:137px">Sign up for our emails</div>
  </div>

  <div class="rule abs" style="left:780px;top:813px;width:265px;border-top:1px solid #ccc"></div>
  <svg class="abs" style="left:780px;top:829px" width="32" height="32" viewBox="0 0 32 32"><path d="M2 2h28v20H14l-8 8v-8H2z" fill="#fff" stroke="var(--orange)" stroke-width="2"/><path d="M7 8h18M7 12h18M7 16h12" stroke="#555" stroke-width="2"/></svg>
  <h2 class="section-title abs" style="left:821px;top:830px;font-size:22px"><em style="color:var(--orange)">Testi</em>monials</h2>
  <div class="quote-mark abs" style="left:764px;top:872px">“</div>
  <p class="test-text abs">Lorem Ipsum is simply dummy text of the printing and typesetting industry. Lorem Ipsum has been the industry's standard dummy text ever since the 1500s, when an unknown printer took a galley of type and scrambled it to make a type specimen book. It has survived not only five centuries.</p>
  <div class="quote-mark abs" style="left:1012px;top:1000px">”</div>
  <div class="rule abs" style="left:783px;top:1040px;width:265px;border-top:1px solid #ccc"></div>
</aside>

<footer class="footer abs">
  <div class="footer-links abs">Home<span>|</span>About Us<span>|</span>Donate<span>|</span>Apply<span>|</span>Pledge<span>|</span>Nominate<span>|</span>Events<span>|</span>Contact<span>|</span>UsDirectors</div>
  <div class="copyright abs">Copyright © 2012 Bright Harbor Proprietary Limited. All Rights Reserved.</div>
</footer>

</body>
</html>
```